Webdesign

We are value investment firm in Denver, Colorado. We are a small but a very unique firm. We are looking for a minimalistic and clean design. We are competing against competitors that usually larger than we are, but we need to have a design that is better than theirs. Our clients put a tremendous trust in us when they let us manage their life savings. This website has to communicate trust but without traditional cliches (dollar bills, glasses, Harbor Ledger Gazette).
We had a coder/designer create our current website a few weeks ago http://brightkestrel.example/tolvan , we are not thrilled about the design. We are attaching our company's presentation, we'd like the design to be closer to the colors of that presentation.
We are looking for both design and coding (wordpress).
Updates
we will pay additional $200 for wordpress implementation
A few points of clarifications about design:
- don't use pictures of strangers
- we are a Denver/Colorado firm, if you use pictures use Denver/Colorado pictures
- full width website is probably what we are looking
- maybe parallax type of design
This theme http://quillframe.example/WP/Nimbra/ is how we see the new design
Industry/Entity Type
Investment

```html
<!DOCTYPE html>
<html lang="en">
<head>
<meta charset="utf-8">
<title>Tolvan Private Portfolio Management</title>
<link rel="stylesheet" href="https://fonts.googleapis.com/css2?family=Noto+Sans:wght@400;700&display=swap">
<style>
:root{
  --nav-blue:#3d72a0;
  --footer-blue:#3e6e99;
  --navy:#1f3a52;
  --heading-blue:#4d86b8;
  --text-dark:#2b2b2b;
  --text-grey:#777;
  --hero-top:#cfe0f1;
  --hero-bottom:#a9cbec;
  --rule:#cde1f3;
  --quote-bg:#e3effa;
  --white:#fff;
  --date:#8db0d0;
}
*{box-sizing:border-box;margin:0;padding:0}
html,body{width:1200px;height:2215px;overflow:hidden}
body{font-family:"Noto Sans",Tahoma,sans-serif;color:var(--text-dark);background:var(--white);position:relative}

/* header */
.site-header{position:absolute;left:0;top:0;width:1200px;height:150px}
.brand{position:absolute;left:120px;top:48px;display:flex;align-items:center;gap:14px;color:var(--navy);font-size:42px;font-weight:700;line-height:52px}
.brand-mark{width:26px;height:26px;background:var(--navy)}
.search{position:absolute;left:810px;top:55px;width:270px;height:40px;border:1px solid #c9d8e6;border-radius:4px;background:#f0f5fa}
.search svg{position:absolute;right:12px;top:8px}

/* nav */
.main-nav{position:absolute;left:0;top:150px;width:1200px;height:80px;background:var(--nav-blue)}
.main-nav ul{list-style:none;display:flex;gap:33px;padding-left:118px;line-height:80px}
.main-nav a{color:var(--white);font-weight:700;font-size:18px;text-decoration:none}

/* hero */
.hero{position:absolute;left:0;top:230px;width:1200px;height:450px;background:radial-gradient(ellipse at 55% 40%,#e0ecf8 0%,var(--hero-top) 35%,var(--hero-bottom) 100%)}
.hero-visual{position:absolute;left:105px;top:105px;width:435px;height:240px;border-radius:20px;background:radial-gradient(ellipse at center,#e9dfc8 0%,#d6c9ad 60%,rgba(200,190,170,0) 100%)}
.hero-goal{position:absolute;left:578px;top:145px;width:490px;height:110px;background:rgba(120,165,210,.55);color:var(--white);font-size:30px;line-height:38px;padding:15px 34px}
.hero-sub{position:absolute;left:588px;top:273px;font-size:27px;color:#1e2b38}
.dots{position:absolute;left:565px;top:412px;display:flex;gap:15px}
.dots span{width:12px;height:12px;border-radius:50%;background:var(--white)}
.dots span.on{background:var(--nav-blue)}

/* features */
.features{position:absolute;left:0;top:680px;width:1200px;height:285px}
.feature{position:absolute;top:28px;width:190px}
.feature .icon{display:block;margin-left:44px}
.feature h3{font-weight:400;font-size:17px;color:var(--heading-blue);margin-top:30px}
.feature h3 b{color:var(--navy);font-weight:400}
.feature p{font-size:14.5px;line-height:18px;margin-top:12px}

/* mission */
.mission{position:absolute;left:0;top:965px;width:1200px;height:173px;background:var(--navy);color:var(--white);font-size:22px;line-height:28px;text-align:center;padding-top:40px;font-weight:700}

/* section headings */
.sec-title{position:absolute;font-size:21px;font-weight:400;color:var(--heading-blue);display:flex;align-items:center;white-space:nowrap}
.sec-title b{font-weight:400;color:var(--navy);margin-left:.3em}
.sec-title::after{content:"";flex:1;height:5px;background:var(--rule);margin-left:12px}
.sec-title.center::before{content:"";flex:1;height:5px;background:var(--rule);margin-right:12px}

.who p{position:absolute;left:120px;top:1213px;width:450px;font-size:14px;line-height:20px}
.read-more{position:absolute;left:120px;top:1373px;font-size:13px;color:var(--nav-blue);display:flex;align-items:center;gap:8px}
.read-more::before{content:"";width:8px;height:8px;background:var(--nav-blue)}

.testimonial .avatar{position:absolute;left:654px;top:1247px;width:58px;height:58px;border-radius:50%;border:3px solid #cfe2f4;background:linear-gradient(#d8b88e,#a88460)}
.testimonial .who-name{position:absolute;left:620px;top:1318px;width:126px;text-align:center;font-size:15px}
.testimonial .who-org{position:absolute;left:620px;top:1340px;width:126px;text-align:center;font-size:13px;color:var(--text-grey)}
.quote{position:absolute;left:785px;top:1218px;width:295px;height:175px;background:var(--quote-bg);font-size:13.5px;line-height:20px;padding:14px 16px}
.quote::before{content:"";position:absolute;left:-14px;top:50px;border:7px solid transparent;border-right-color:var(--quote-bg)}

.team .member{position:absolute;top:1468px;width:232px}
.team .photo{height:233px;background:linear-gradient(#7a7a7a,#3f3f3f)}
.team .name{text-align:center;font-size:15px;margin-top:14px}
.team .role{text-align:center;font-size:13px;color:var(--text-grey);margin-top:2px}

/* footer */
.site-footer{position:absolute;left:0;top:1800px;width:1200px;height:355px;background:var(--footer-blue);color:var(--white)}
.col{position:absolute;top:20px;width:220px}
.col h4{font-size:14px;font-weight:700;margin-bottom:16px}
.articles li{list-style:none;font-size:13px;line-height:18px;padding-left:16px;position:relative;margin-bottom:14px}
.articles li::before{content:"";position:absolute;left:2px;top:7px;width:4px;height:4px;border-radius:50%;background:var(--white)}
.articles time{display:block;color:var(--date)}
.news li{list-style:none;font-size:13px;line-height:18px;padding:10px 0 12px;border-bottom:1px solid #8eb0cf}
.news li:first-child{padding-top:0}
.book{display:flex;gap:12px;margin-bottom:20px;font-size:13px;line-height:17px}
.book .cover{flex:0 0 64px;height:88px;background:linear-gradient(#c48a3c,#6b4a25)}
.book .cover.light{background:linear-gradient(#e8e8e8,#b5b5b5)}
.contact div{display:flex;gap:12px;font-size:13px;line-height:18px;margin-bottom:20px}
.contact svg{flex:0 0 16px;margin-top:2px}

.bottom-bar{position:absolute;left:0;top:2155px;width:1200px;height:60px;font-size:13px;color:var(--text-dark)}
.bottom-bar .copy{position:absolute;left:120px;top:22px}
.bottom-bar .links{position:absolute;right:120px;top:22px}
.bottom-bar .links span{padding:0 8px}
.bottom-bar .links span+span{border-left:1px solid #333}
</style>
</head>
<body>

<header class="site-header">
  <div class="brand"><span class="brand-mark"></span><span>Tolvan</span></div>
  <div class="search">
    <svg width="24" height="24" viewBox="0 0 24 24"><circle cx="9" cy="9" r="6.5" fill="none" stroke="#2f5f8c" stroke-width="2.5"/><line x1="14" y1="14" x2="21" y2="21" stroke="#2f5f8c" stroke-width="3.5" stroke-linecap="round"/></svg>
  </div>
</header>

<nav class="main-nav">
  <ul>
    <li><a>TOLVAN</a></li><li><a>ABOUT US</a></li><li><a>INVEST DIFFERENTY</a></li><li><a>CONTENT</a></li><li><a>CAREER</a></li><li><a>CONTACT US</a></li>
  </ul>
</nav>

<section class="hero">
  <div class="hero-visual" role="img" aria-label="Four cloth money bags marked with currency symbols"></div>
  <div class="hero-goal">Our Goal is to preserve and grow our clients’ wealth</div>
  <div class="hero-sub">While letting them sleep well at night</div>
  <div class="dots"><span class="on"></span><span></span><span></span></div>
</section>

<section class="features">
  <div class="feature" style="left:120px">
    <svg class="icon" width="58" height="58" viewBox="0 0 58 58"><circle cx="29" cy="29" r="29" fill="#3d72a0"/><g fill="#fff"><circle cx="21" cy="19" r="4"/><circle cx="29" cy="17" r="4.5"/><circle cx="37" cy="19" r="4"/><rect x="16" y="25" width="9" height="18" rx="3"/><rect x="24" y="24" width="10" height="21" rx="3"/><rect x="33" y="25" width="9" height="18" rx="3"/></g></svg>
    <h3>We Are <b>Different</b></h3>
    <p>Our Active Value investment approach is crafted specifically for today’s treacherous sideways markets.</p>
  </div>
  <div class="feature" style="left:369px">
    <svg class="icon" width="58" height="58" viewBox="0 0 58 58"><circle cx="29" cy="29" r="29" fill="#3d72a0"/><g fill="#fff"><circle cx="23" cy="22" r="9"/><rect x="28" y="30" width="16" height="4" rx="2"/><rect x="28" y="35" width="16" height="4" rx="2"/><rect x="28" y="40" width="16" height="4" rx="2"/><rect x="14" y="35" width="12" height="4" rx="2"/><rect x="14" y="40" width="12" height="4" rx="2"/></g><circle cx="23" cy="22" r="4.5" fill="none" stroke="#3d72a0" stroke-width="2"/></svg>
    <h3>Investment <b>Process</b></h3>
    <p>The pillars of investment process: 1 Discovery<br>2 Research<br>3 Maintenance<br>4 Selling</p>
  </div>
  <div class="feature" style="left:627px">
    <svg class="icon" width="58" height="58" viewBox="0 0 58 58"><circle cx="29" cy="29" r="29" fill="#3d72a0"/><rect x="15" y="16" width="28" height="20" rx="3" fill="#fff"/><text x="29" y="31" text-anchor="middle" font-size="12" font-weight="700" fill="#3d72a0" font-family="Noto Sans,sans-serif">AD</text><rect x="27" y="36" width="4" height="10" fill="#fff"/></svg>
    <h3>Sideways <b>Market</b></h3>
    <p>Every long-lasting bull market of the past two centuries was followed by a sideways market that lasted about 15 years.</p>
  </div>
  <div class="feature" style="left:876px">
    <svg class="icon" width="58" height="58" viewBox="0 0 58 58"><circle cx="29" cy="29" r="29" fill="#3d72a0"/><g stroke="#fff" stroke-width="5" stroke-linecap="round"><line x1="20" y1="38" x2="36" y2="22"/><line x1="22" y1="20" x2="38" y2="38"/></g><circle cx="38" cy="20" r="5" fill="#fff"/></svg>
    <h3>Why We <b>Build Models</b></h3>
    <p>Building models is important for us. Models help us to understand businesses better. They provide insights as to which metrics matter and which don’t.</p>
  </div>
</section>

<section class="mission">A disciplined, process-driven, value investment firm that provides a private portfolio<br>management service tailored to individual and institutional clients tired of in-the-box,<br>cookie-cutter, buy-and-hope investment products.</section>

<section class="who">
  <h2 class="sec-title" style="left:120px;top:1160px;width:442px">Who<b>We Are</b></h2>
  <p>Tolvan is a state registered investment advisor, we are registered with our home state of Colorado. We are also registered with other states as needed or will pursue registration as the need arises. We provide personal investment management services to individuals, institutions and foundations through separately managed accounts consisting of individual securities (stocks, bonds and money market).</p>
  <div class="read-more">READ MORE</div>
</section>

<section class="testimonial">
  <h2 class="sec-title" style="left:604px;top:1160px;width:476px">What People<b>Are Saying</b></h2>
  <div class="avatar" role="img" aria-label="Portrait of the client"></div>
  <div class="who-name">Nora Ellison</div>
  <div class="who-org">Nora Kids Care</div>
  <div class="quote">Duis sit amet orci et lectus dictum auctor a nec enim. Donec suscipit fringilla elementum. Suspendisse nec justo ut felis ornare tincidunt vitae et lectus. In iaculis mauris luctus massa pellentesque blandit. Integer et neque. Nulla vitae dictum nisi, ut ultrices tortor.</div>
</section>

<section class="team">
  <h2 class="sec-title center" style="left:120px;top:1413px;width:960px">Our<b>Team</b></h2>
  <div class="member" style="left:120px"><div class="photo" role="img" aria-label="Portrait of the president"></div><div class="name">Harold J. Brenner, CFA</div><div class="role">President and Founder</div></div>
  <div class="member" style="left:362px"><div class="photo" role="img" aria-label="Portrait of the director of operations"></div><div class="name">Marla Fenwick</div><div class="role">Director of Operations</div></div>
  <div class="member" style="left:604px"><div class="photo" role="img" aria-label="Portrait of the chief investment officer"></div><div class="name">Dorian K. Vashko, CFA</div><div class="role">Chief Investment Officer</div></div>
  <div class="member" style="left:846px"><div class="photo" role="img" aria-label="Portrait of the client services lead"></div><div class="name">Lena Vashko</div><div class="role">Client services</div></div>
</section>

<footer class="site-footer">
  <div class="col articles" style="left:120px">
    <h4>RECENT ARTICLES</h4>
    <ul>
      <li>The True Value of Macro Forecasting for Value Investors<time>May 20, 2014</time></li>
      <li>The Modern Portfolio Theory Flat Earth Society<time>May 11, 2014</time></li>
      <li>Crony Capitalism and the Sage of Elm Street<time>May 8, 2014</time></li>
      <li>An Investor’s Guide to Better Writing — Seriously<time>May 11, 2014</time></li>
    </ul>
  </div>
  <div class="col news" style="left:362px">
    <h4>IN THE NEWS</h4>
    <ul>
      <li>Lorem ipsum dolor sit amet, consectetur adipiscing elit</li>
      <li>Lorem ipsum dolor sit amet, consectetur adipiscing elit</li>
      <li>Lorem ipsum dolor sit amet, consectetur adipiscing elit</li>
      <li>Lorem ipsum dolor sit amet, consectetur adipiscing elit</li>
    </ul>
  </div>
  <div class="col" style="left:604px">
    <h4>BOOKS</h4>
    <div class="book"><div class="cover" role="img" aria-label="Book cover"></div><p>Patient Value Investing was written for diehard professional investors – it had 75 tables and charts and was a fairly technical book</p></div>
    <div class="book"><div class="cover light" role="img" aria-label="Book cover"></div><p>The Short Book of Flat Markets was published in October 2010. This book had only five charts and was one third the former book’s size.</p></div>
  </div>
  <div class="col contact" style="left:846px">
    <h4>CONTACT US</h4>
    <div><svg width="16" height="18" viewBox="0 0 16 18"><path d="M8 0a6 6 0 0 0-6 6c0 5 6 12 6 12s6-7 6-12a6 6 0 0 0-6-6z" fill="#fff"/><circle cx="8" cy="6" r="2.3" fill="#3e6e99"/></svg><span>4120 Juniper Ridge Blvd,<br>Suite 210E, Aspen Grove<br>CO 80199-0000</span></div>
    <div><svg width="16" height="16" viewBox="0 0 16 16"><path d="M3 1l3 3-1.5 2.5a9 9 0 0 0 5 5L12 10l3 3-2 2.5C7 15 1 9 .5 3z" fill="#fff"/></svg><span>303.555.0148<br>888.555.0172</span></div>
    <div><svg width="16" height="16" viewBox="0 0 16 16"><rect x="1" y="5" width="14" height="9" rx="1" fill="#fff"/><rect x="4" y="1" width="8" height="5" fill="#fff"/><rect x="4" y="9" width="8" height="1.5" fill="#3e6e99"/></svg><span>303.555.0193</span></div>
    <div><svg width="16" height="14" viewBox="0 0 16 14"><rect x="1" y="2" width="14" height="10" fill="#fff"/><path d="M1 2l7 6 7-6" fill="none" stroke="#3e6e99" stroke-width="1.3"/></svg><span>contact@tolvan.example</span></div>
  </div>
</footer>

<div class="bottom-bar">
  <div class="copy">Copyright © 2014 Tolvan</div>
  <div class="links"><span>Terms &amp; Conditon</span><span>Privacy Policy</span></div>
</div>

</body>
</html>
```